Walk Bold Stay Kind Ebook and Print book cover

I need a professional, eye catching cover that will stand out. The title of the book is "Walk Bold Stay Kind: 47 Quiet Rules For Calm and Wonder" It is a self-help personal transformation book by author Dale Ormsby. The cover will be on both print and ebook covers. I want something that is similar yet different to best-selling books in the genre, nothing too boring. A blue background might work, but it isn't a requirement. I'm open to other colors as long as it's powerful, professional, and screams "Buy me because this book is going to change your life!"
Updates

So far, 3 designs (3 of the 4 star rated designs) are in contention, but they all can be improved. I think the book cover should best convey "thinking smart" in a dynamic way. I'll run another poll in a day or so when I get additional designs I like. Added Thursday, May 4, 2017

Based on current designs, I wanted to provide additional guidance. The title and image should pop and be clearly visible at a distance as a thumbnail. Also, I'm wanting something bold and creative but not too confusing. I currently have a couple solid designs that are in contention to win, but I have another 7 days left for the project. I extended it to 10 days from the initial 5. I'll include several more polls for my followers and will likely pick the top ranking design based off the series of polls and will be eliminating lower ranking designs with each new poll and set of promising designs that come in. Finally, I may ask to see what the back will look like on the print version since I'll need both the Lumora and print (5" by 8") designs. Added Saturday, May 6, 2017

It's been recommended by some that I should have my own picture on the cover. I'm not completely convinced, but I would like to see some additional designs that incorporate my photo (touched up to remove the shine from my forehead and the label brand name removed from the t-shire) into a cover design. I have several good designs coming in, so typeset and professional looking font is extremely important. Blue is also preferred but not required. I've attached the photo on the brief for those who want to submit a design with that photo. Added Saturday, May 6, 2017

Target Market(s)

Working age adults seeking personal transformation and self improvement.

Industry/Entity Type

Motivation

Requirements
Must have
• Creativity. Eye catching. Striking. Contrast. Looks good close up and as a thumbnail at a distance. Font should be easy to read and pop from the cover along with the design.
Nice to have
• Powerful image placement. Play up the "Walk Bold" aspect of the title. Perhaps even contrasting someone who's thinking "Hard." Here are a few examples of intriguing covers (though not necessarily related to the genre) I like mainly for aesthetics and creativity. https://www.shopvale.com/dp/Q71MRT2KWD/ https://www.shopvale.com/dp/Q34PLN8XEA
• https://www.shopvale.com/dp/Q925GHV3TC/
• https://www.shopvale.com/dp/Q48DJW6RZB/
• (the font is a little poor in the last one but the image is evoking)
Should not have
• Ugly, tacky, or hard to read fonts. A simple photo with text on top. A simple background with words. Confusing images. Designs with no additional stock image purchase requirements will be given preference over those that do. I've seen a lot of balloons and light bulbs. I'm not saying you can't include them in the design, but if you want to stand out, try to find something more creative that expresses the concept of the title.

```html
<!DOCTYPE html>
<html lang="en">
<head>
<meta charset="utf-8">
<title>Walk Bold Stay Kind — Print Cover</title>
<link href="https://fonts.googleapis.com/css2?family=Bebas+Neue&family=Montserrat:wght@600&family=Playfair+Display:wght@400;700&display=swap" rel="stylesheet">
<style>
  :root {
    --gold-light: #dba63c;
    --gold-mid: #a8761f;
    --gold-dark: #3a270c;
    --ink: #0c0a08;
    --spine-yellow: #f2e21a;
    --white: #ffffff;
    --sunset-top: #d9681c;
    --sunset-mid: #b9481a;
    --sunset-low: #f09a38;
    --silhouette: #0a0705;
    --label-gold: #c9962e;
    --label-ink: #2a1d08;
    --ornament: #d9ad55;
  }
  html, body { margin: 0; padding: 0; overflow: hidden; background: #ffffff; }
  .cover {
    position: relative;
    width: 1200px;
    height: 885px;
    overflow: hidden;
    font-family: "Bebas Neue", sans-serif;
  }
  .trim {
    position: absolute;
    border: 1px dashed rgba(255,255,255,0.85);
    pointer-events: none;
  }

  /* Back cover */
  .back {
    position: absolute; left: 0; top: 0; width: 568px; height: 885px;
    background:
      radial-gradient(ellipse at 40% 30%, rgba(255,220,130,0.35), transparent 60%),
      linear-gradient(180deg, var(--gold-light) 0%, var(--gold-mid) 45%, #6b4814 75%, var(--gold-dark) 100%);
  }
  .back .trim { left: 16px; top: 15px; right: 0; bottom: 15px; border-right: none; }
  .back-author {
    position: absolute; left: 42px; top: 42px;
    font-family: "Montserrat", sans-serif; font-weight: 600;
    font-size: 27px; letter-spacing: 2.5px; color: var(--ink);
    padding-bottom: 2px; border-bottom: 2px solid var(--ink);
    text-transform: uppercase; line-height: 1.1;
  }
  .back-title {
    position: absolute; left: 46px; top: 268px;
    font-size: 50px; color: var(--white); letter-spacing: 0.5px; line-height: 1;
  }
  .subtitle-box {
    position: absolute; left: 46px; top: 326px; width: 491px; height: 215px;
    border: 2px solid var(--ink); border-radius: 8px; box-sizing: border-box;
    font-family: "Playfair Display", serif; color: var(--white);
  }
  .subtitle-box .numeral {
    position: absolute; left: 34px; top: 12px;
    font-size: 150px; line-height: 1; letter-spacing: -4px;
  }
  .subtitle-box .lead {
    position: absolute; left: 226px; top: 26px;
    font-size: 54px; line-height: 1;
  }
  .subtitle-box .line2 {
    position: absolute; left: 226px; top: 92px;
    font-size: 38px; line-height: 1;
  }
  .subtitle-box .line3 {
    position: absolute; left: 226px; top: 140px;
    font-size: 27px; line-height: 1;
  }
  .ornament {
    position: absolute; left: 198px; top: 530px; width: 186px; height: 22px;
    background: var(--ornament); border-radius: 11px; opacity: 0.85;
  }
  .credits {
    position: absolute; left: 42px; top: 748px;
    font-size: 16px; color: var(--white); line-height: 1.35; letter-spacing: 0.3px;
  }
  .credits p { margin: 0 0 14px; }
  .logo-slot {
    position: absolute; left: 339px; top: 740px; width: 184px; height: 109px;
    background: var(--label-gold);
    display: flex; align-items: center; justify-content: center; text-align: center;
    font-family: Arial, Helvetica, sans-serif; font-size: 24px; line-height: 1.15;
    color: var(--label-ink);
  }

  /* Spine */
  .spine {
    position: absolute; left: 568px; top: 0; width: 63px; height: 885px;
    background: var(--ink);
  }
  .spine .trim { left: 8px; right: 8px; top: 28px; bottom: 28px; border-color: rgba(255,255,255,0.7); }
  .spine-dots {
    position: absolute; left: 20px; width: 22px; height: 0;
    border-top: 2px dotted var(--spine-yellow);
  }
  .spine-title, .spine-author {
    position: absolute; left: 50%; color: var(--spine-yellow);
    writing-mode: vertical-rl; transform: translateX(-50%);
    white-space: nowrap;
  }
  .spine-title { top: 322px; font-size: 28px; letter-spacing: 0.5px; }
  .spine-author { top: 740px; font-family: "Montserrat", sans-serif; font-weight: 600; font-size: 13px; letter-spacing: 1.5px; }

  /* Front cover */
  .front {
    position: absolute; left: 631px; top: 0; width: 569px; height: 885px;
  }
  .front .sky {
    position: absolute; inset: 0;
    background:
      radial-gradient(ellipse at 70% 62%, rgba(255,190,80,0.6), transparent 55%),
      linear-gradient(180deg, var(--sunset-top) 0%, var(--sunset-mid) 38%, var(--sunset-low) 68%, #7a2c10 100%);
  }
  .front .figure-area {
    position: absolute; left: 0; top: 250px; width: 320px; height: 635px;
    background: linear-gradient(180deg, #1a0f08 0%, var(--silhouette) 40%);
    border-radius: 50% 55% 0 0 / 28% 34% 0 0;
  }
  .front .skyline {
    position: absolute; left: 0; right: 0; bottom: 0; height: 120px;
    background: linear-gradient(180deg, rgba(10,7,5,0) 0%, rgba(10,7,5,0.85) 55%, var(--silhouette) 100%);
  }
  .front .trim { left: 0; top: 15px; right: 16px; bottom: 15px; border-left: none; }
  .front-title {
    position: absolute; right: 42px; top: 28px; margin: 0;
    color: var(--white); font-weight: 400; text-align: right; line-height: 1;
  }
  .front-title span { display: block; }
  .front-title .t1 { font-size: 134px; letter-spacing: 19px; margin-right: -19px; }
  .front-title .t2 { font-size: 92px; letter-spacing: 5px; margin-top: 6px; margin-right: -5px; }
  .front-title .t3 { font-size: 92px; letter-spacing: 27px; margin-top: 6px; margin-right: -27px; }
  .front-author {
    position: absolute; left: 300px; top: 826px; transform: translateX(-50%);
    font-family: "Montserrat", sans-serif; font-weight: 600; white-space: nowrap;
    font-size: 28px; letter-spacing: 3px; color: var(--white);
    text-transform: uppercase;
  }
</style>
</head>
<body>
<div class="cover">

  <section class="back">
    <div class="trim"></div>
    <div class="back-author">Dale Ormsby</div>
    <div class="back-title">WALK BOLD STAY KIND</div>
    <div class="subtitle-box">
      <span class="numeral">47</span>
      <span class="lead">Quiet</span>
      <span class="line2">Rules For</span>
      <span class="line3">Calm and Wonder</span>
    </div>
    <div class="ornament" role="img" aria-label="Gold flourish ornament"></div>
    <div class="credits">
      <p>THE AUTHOR'S:<br>DALE ORMSBY</p>
      <p>THE PUBLISHER WILL BE:<br>YOUR NAME</p>
    </div>
    <div class="logo-slot">LOGO<br>OR<br>BARCODE</div>
  </section>

  <section class="spine">
    <div class="trim"></div>
    <div class="spine-dots" style="top:12px"></div>
    <div class="spine-dots" style="bottom:12px"></div>
    <div class="spine-title">WALK BOLD STAY KIND</div>
    <div class="spine-author">DALE ORMSBY</div>
  </section>

  <section class="front">
    <div class="sky" role="img" aria-label="Orange sunset sky with glowing clouds"></div>
    <div class="skyline" role="img" aria-label="Dark city skyline along the horizon"></div>
    <div class="figure-area" role="img" aria-label="Black silhouette of a thinking person resting chin on hand"></div>
    <div class="trim"></div>
    <h1 class="front-title">
      <span class="t1">WALK</span>
      <span class="t2">BOLD STAY</span>
      <span class="t3">KIND</span>
    </h1>
    <div class="front-author">Dale Ormsby</div>
  </section>

</div>
</body>
</html>
```